Contemporary new French wine brand needs logo and series of label design

to design a new contemporary logo and series of labels for a new French wine brand. We hope to attract not just current French wine drinkers but new ones who may appreciate a less traditional and more modern style.
Updates

Reason: we are wanting to extend the project for a few days more to receive more submissions since we had fewer designs submitted than we were expecting, maybe because of the holidays.

Target Market(s)

people who follow the arts community (eg. music, theatre, visual/video arts, dance) --- all mature ages.

Industry/Entity Type

French Wine

Requirements
Must have
• a clear, memorable treatment for the name CLAVINE with accompanying logo.
Nice to have
• embossing, matte/gloss refinement, tasteful foil stamping, coated stock for the whites to help the integrity of the paper in and out of ice buckets. A combo of say, three types of fonts; a semi custom font for the brand name Clavine and maybe a script and one other.
Should not have
• not traditional French

```html
<!DOCTYPE html>
<html lang="en">
<head>
<meta charset="utf-8">
<title>Clavine — Wine Label Series</title>
<link rel="stylesheet" href="https://fonts.googleapis.com/css2?family=Jost:wght@600&family=Dancing+Script:wght@500&family=Montserrat:wght@700&display=swap">
<style>
  :root {
    --backdrop: #3b3b3b;
    --paper: #ffffff;
    --paper-cream: #fbf8ee;
    --ink: #111111;
    --tone-deep: #5c5c5c;
    --tone-mid: #808080;
    --tone-soft: #a3a3a3;
    --tone-gold-deep: #cbbf9c;
    --tone-gold-soft: #ece5d0;
    --gold: #a8874e;
    --gold-bar-start: #d8c9a2;
    --gold-bar-end: #8a7550;
    --rose: #b4536a;
    --rose-ink: #5a513e;
  }
  * { box-sizing: border-box; margin: 0; padding: 0; }
  html, body { width: 1200px; height: 406px; overflow: hidden; }
  body { background: var(--backdrop); position: relative; }

  .label {
    position: absolute;
    top: 74px;
    width: 168px;
    height: 258px;
    background: var(--paper);
    overflow: hidden;
  }
  .label--cabernet-franc { left: 19px; }
  .label--sauvignon-blanc { left: 274px; }
  .label--rose { left: 538px; background: var(--paper-cream); }
  .label--muscadet { left: 782px; }
  .label--cabernet-sauvignon { left: 1023px; }

  .label__pattern {
    position: absolute;
    left: 0; right: 0; top: 8px; bottom: 8px;
  }
  .label__pattern--waves {
    background: linear-gradient(155deg, var(--tone-deep) 0%, var(--tone-mid) 45%, var(--tone-soft) 70%, var(--tone-mid) 100%);
  }
  .label__pattern--leaves {
    top: 10px; bottom: 10px;
    background: radial-gradient(ellipse at 30% 35%, var(--tone-soft), var(--tone-mid) 60%, var(--tone-deep) 100%);
  }
  .label__pattern--gold-leaves {
    top: 6px; bottom: 6px;
    background: radial-gradient(ellipse at 50% 50%, var(--tone-gold-soft), var(--tone-gold-deep) 90%);
  }
  .label__pattern--chevron {
    background: linear-gradient(90deg, var(--tone-deep) 0%, var(--tone-mid) 30%, var(--tone-soft) 50%, var(--tone-mid) 70%, var(--tone-deep) 100%);
  }
  .label__pattern--herringbone {
    left: 4px; right: 4px;
    background: linear-gradient(90deg, var(--tone-mid), var(--tone-deep) 33%, var(--tone-mid) 34%, var(--tone-deep) 66%, var(--tone-mid) 67%, var(--tone-deep));
  }

  .label__band {
    position: absolute; left: 0; right: 0; height: 10px; background: var(--ink);
  }
  .label__band--top { top: 0; }
  .label__band--bottom { bottom: 0; }

  .panel {
    position: absolute;
    background: var(--paper);
    display: flex;
    flex-direction: column;
    align-items: center;
    text-align: center;
  }
  .panel::before {
    content: "";
    position: absolute; left: 0; right: 0; top: 0;
    height: 7px; background: var(--ink);
  }
  .label--rose .panel { background: var(--paper-cream); }
  .label--rose .panel::before { background: linear-gradient(90deg, var(--gold-bar-start), var(--gold-bar-end)); }

  .label--cabernet-franc .panel { left: 71px; width: 88px; top: 137px; height: 113px; }
  .label--sauvignon-blanc .panel { left: 68px; width: 77px; top: 31px; height: 113px; }
  .label--rose .panel { left: 41px; width: 87px; top: 68px; height: 112px; }
  .label--muscadet .panel { left: 41px; width: 88px; top: 68px; height: 112px; }
  .label--cabernet-sauvignon .panel { left: 44px; width: 89px; top: 137px; height: 113px; }

  .brand {
    margin-top: 18px;
    font-family: "Jost", sans-serif;
    font-weight: 600;
    font-size: 10px;
    letter-spacing: 0.6em;
    padding-left: 0.6em;
    color: var(--ink);
  }
  .label--sauvignon-blanc .brand { letter-spacing: 0.5em; padding-left: 0.5em; }
  .label--rose .brand { color: #3a3426; }

  .varietal {
    margin-top: 24px;
    font-family: "Dancing Script", cursive;
    font-weight: 500;
    font-size: 11px;
    color: var(--gold);
    white-space: nowrap;
  }
  .label--cabernet-sauvignon .varietal { font-size: 10px; }
  .label--muscadet .varietal { font-size: 15px; margin-top: 20px; }
  .label--rose .varietal { color: var(--rose); }

  .origin {
    margin-top: auto;
    font-family: "Montserrat", sans-serif;
    font-weight: 700;
    font-size: 5.5px;
    color: var(--ink);
    padding-bottom: 1px;
    border-bottom: 0.7px solid var(--ink);
    width: 52px;
  }
  .volume {
    margin: 2px 0 11px;
    font-family: "Montserrat", sans-serif;
    font-weight: 700;
    font-size: 3.8px;
    letter-spacing: 0.3em;
    color: var(--ink);
  }
  .label--rose .origin, .label--rose .volume { color: var(--rose-ink); border-color: var(--rose-ink); }
</style>
</head>
<body>
  <main class="label-series">
    <section class="label label--cabernet-franc">
      <div class="label__pattern label__pattern--waves" role="img" aria-label="Black and white diagonal wavy stripe pattern"></div>
      <div class="panel">
        <p class="brand">CLAVINE</p>
        <p class="varietal">Cabernet Franc</p>
        <p class="origin">Made in France</p>
        <p class="volume">750ml</p>
      </div>
    </section>

    <section class="label label--sauvignon-blanc">
      <div class="label__band label__band--top"></div>
      <div class="label__pattern label__pattern--leaves" role="img" aria-label="Black line-drawn palm leaf pattern on white"></div>
      <div class="label__band label__band--bottom"></div>
      <div class="panel">
        <p class="brand">CLAVINE</p>
        <p class="varietal">Sauvignon Blanc</p>
        <p class="origin">Made in France</p>
        <p class="volume">750ml</p>
      </div>
    </section>

    <section class="label label--rose">
      <div class="label__pattern label__pattern--gold-leaves" role="img" aria-label="Gold line-drawn palm leaf pattern on cream"></div>
      <div class="panel">
        <p class="brand">CLAVINE</p>
        <p class="varietal">Rose de Provence</p>
        <p class="origin">Made in France</p>
        <p class="volume">750ml</p>
      </div>
    </section>

    <section class="label label--muscadet">
      <div class="label__pattern label__pattern--chevron" role="img" aria-label="Black and white diagonal chevron stripe pattern"></div>
      <div class="panel">
        <p class="brand">CLAVINE</p>
        <p class="varietal">Muscadet</p>
        <p class="origin">Made in France</p>
        <p class="volume">750ml</p>
      </div>
    </section>

    <section class="label label--cabernet-sauvignon">
      <div class="label__pattern label__pattern--herringbone" role="img" aria-label="Black and white herringbone stripe pattern"></div>
      <div class="panel">
        <p class="brand">CLAVINE</p>
        <p class="varietal">Cabernet Sauvignon</p>
        <p class="origin">Made in France</p>
        <p class="volume">750ml</p>
      </div>
    </section>
  </main>
</body>
</html>
```